Metal head/ Sushi chef wanting artistic yet high imact business card

I'm sushi chef for make living in Australia originally from Tokyo Japan.
I'm also guitarist/composer as well on progressive metalcore/djent genre.
My favorite visual art is Mandala. Sacred geometries, Fractals, Paisleys are also things fit in me. I like dark color, earth color, and sometimes psychedelic patterns.
I want to hand out my business card when I meet new people in music industries or someone who is wanting private sushi chef for their party.
I know metal and sushi are far different subjects but they are all my passion. I would like to work with the designer who can create something cool from information above.

https://www.viewtrove.com/channel/QX7h4LpRzd2VnWe9kT3BFs8j
https://tunebarrel.com/user-817264093

Front
my name, Kenjiro Motsuba
occupation, "Sushi chef" "Metal guitarist/composer"
Email address, velmoquartz@mailorb.com
Phone number, (61)498271053

Back:
My Viewtrove channel, Pagefolk, Tunebarrel, Glintory. All of those are searchable by "Velmoquartz" The website mentioned above can be described as their logos.

Target Market(s)

people in Music industry, such as musicians, venue managers, promoters.
People who wants to have private sushi chef for their private function, party or events.

Industry/Entity Type

Artists

Contact Information for Business Card

Uploaded photos are just image reference. not thinking to use them.
My details:
I like :
energetic music that has a lot of details such as Progressive metalcore, jazz, djent, psychedelic music.
Spiritual thoughs, Buddism, fundamentals, relaxation music, 420, weed culture, Free thoughts
U.S street culture, skate board, kelps, surf, bicycle, nature, camping, hiking, ocean, mountain, desert, countryside,
permaculture, natural farming, organic farming, compost, self sufficient.
nigiri sushi, art sushi, something/someone beautiful in mind.

Dislike:
Fakes, Bullshits, format, negative, preservatives, artificial colors, illuminati, satanism, manipulation, mass favorites, big society, politics, Chinese letters on western design

Colors
0455a3
000000
7c7c7c
00a990
acd036
f37122

Requirements
Must have
• Front
• my name, Kenjiro Motsuba
• occupation, "Sushi chef" "Metal guitarist/composer"
• Email address, velmoquartz@mailorb.com
• Phone number, (61)498271053
• Back:
• My Viewtrove channel, Pagefolk, Tunebarrel, Glintory. All of those are searchable by "Velmoquartz" The website mentioned above can be described as their logos.
Nice to have
• something based on one of those either back ground or logo:
• Mandala, Sacred Geometry, Fractal art
Should not have
• pop essence. mass favorites, pink, Chinese letters, asian fonts, something asian

```html
<!DOCTYPE html>
<html lang="en">
<head>
<meta charset="utf-8">
<title>Kenjiro Motsuba – Business Card</title>
<link rel="stylesheet" href="https://fonts.googleapis.com/css2?family=Arimo:wght@400&family=Lato:wght@400&family=Lobster&display=swap">
<style>
  :root {
    --stage: #171717;
    --card: #242424;
    --card-light: #313131;
    --emboss: #1c1c1c;
    --emboss-edge: #3a3a3a;
    --silver: #d6d6d6;
    --silver-dim: #9a9a9a;
    --blue: #1a63c4;
    --white: #f2f2f2;
  }
  * { box-sizing: border-box; margin: 0; padding: 0; }
  html, body { width: 1200px; height: 900px; overflow: hidden; }
  body {
    background: var(--stage);
    position: relative;
    font-family: "Lato", sans-serif;
  }
  .card {
    position: absolute;
    left: 250px;
    width: 700px;
    height: 400px;
    background: linear-gradient(135deg, var(--card-light), var(--card) 60%);
    overflow: hidden;
    box-shadow: 0 10px 30px rgba(0,0,0,0.5);
  }
  .card--front { top: 35px; }
  .card--back { top: 465px; }

  .ornament {
    position: absolute;
    width: 140px;
    height: 130px;
  }
  .ornament--embossed {
    background: linear-gradient(135deg, #222 0%, var(--emboss) 100%);
    box-shadow: inset 1px 1px 0 var(--emboss-edge), inset -1px -1px 0 #111;
  }
  .ornament--silver {
    background: linear-gradient(135deg, var(--silver) 0%, var(--silver-dim) 55%, #6e6e6e 100%);
    opacity: 0.55;
  }
  .ornament--tl { top: 0; left: 0; border-bottom-right-radius: 100%; }
  .ornament--bl { bottom: 0; left: 0; border-top-right-radius: 100%; }
  .ornament--tr { top: 0; right: 0; border-bottom-left-radius: 100%; }
  .ornament--br { bottom: 0; right: 0; border-top-left-radius: 100%; }

  .front-name {
    position: absolute;
    top: 150px;
    left: 0;
    width: 100%;
    text-align: center;
    font-family: "Lobster", cursive;
    font-weight: 400;
    font-size: 62px;
    color: var(--silver);
  }
  .front-name__first { color: #151515; text-shadow: 0 1px 0 #3c3c3c; }

  .identity {
    position: absolute;
    top: 160px;
    right: 312px;
    text-align: right;
  }
  .identity__name {
    font-family: "Arimo", sans-serif;
    font-weight: 400;
    font-size: 32px;
    color: var(--blue);
    letter-spacing: 0.5px;
    line-height: 1;
  }
  .identity__role {
    margin-top: 8px;
    font-size: 18px;
    color: var(--white);
  }
  .divider {
    position: absolute;
    left: 400px;
    top: 158px;
    width: 2px;
    height: 72px;
    background: var(--blue);
  }
  .contacts {
    position: absolute;
    left: 416px;
    top: 158px;
    list-style: none;
  }
  .contacts__item {
    display: flex;
    align-items: center;
    gap: 10px;
    font-size: 18px;
    color: var(--white);
    line-height: 24px;
  }
  .contacts__icon { width: 12px; height: 12px; flex: none; }

  .socials {
    position: absolute;
    top: 296px;
    left: 0;
    width: 640px;
    text-align: center;
  }
  .socials__list {
    display: flex;
    justify-content: center;
    gap: 14px;
    list-style: none;
    font-size: 15px;
    color: var(--blue);
  }
  .socials__handle {
    margin-top: 6px;
    font-size: 22px;
    color: var(--white);
    letter-spacing: 0.5px;
  }
</style>
</head>
<body>
  <section class="card card--front" aria-label="Card front">
    <div class="ornament ornament--embossed ornament--tl" role="img" aria-label="Embossed mandala ornament"></div>
    <div class="ornament ornament--embossed ornament--bl" role="img" aria-label="Embossed mandala ornament"></div>
    <div class="ornament ornament--silver ornament--tr" role="img" aria-label="Silver foil mandala ornament"></div>
    <div class="ornament ornament--silver ornament--br" role="img" aria-label="Silver foil mandala ornament"></div>
    <h1 class="front-name"><span class="front-name__first">Kenjiro</span> Motsuba</h1>
  </section>

  <section class="card card--back" aria-label="Card back">
    <div class="ornament ornament--embossed ornament--tl" role="img" aria-label="Embossed mandala ornament"></div>
    <div class="ornament ornament--embossed ornament--bl" role="img" aria-label="Embossed mandala ornament"></div>
    <div class="ornament ornament--silver ornament--tr" role="img" aria-label="Silver foil mandala ornament"></div>
    <div class="ornament ornament--silver ornament--br" role="img" aria-label="Silver foil mandala ornament"></div>

    <div class="identity">
      <h2 class="identity__name">KENJIRO MOTSUBA</h2>
      <p class="identity__role">Sushi chef,Metal guitarist/composer</p>
    </div>
    <div class="divider"></div>
    <ul class="contacts">
      <li class="contacts__item">
        <svg class="contacts__icon" viewBox="0 0 12 12"><path d="M2 1 L4 1 L5 4 L3.6 5 Q5 7.5 7 8.4 L8 7 L11 8 L11 10 Q10 11 8.5 11 Q2 9 1 3 Q1 2 2 1 Z" fill="var(--blue)"/></svg>
        (61) 49827 1053
      </li>
      <li class="contacts__item">
        <svg class="contacts__icon" viewBox="0 0 12 12"><rect x="0.7" y="2.2" width="10.6" height="7.6" fill="none" stroke="var(--blue)" stroke-width="1.2"/><path d="M1 2.6 L6 6.6 L11 2.6" fill="none" stroke="var(--blue)" stroke-width="1.2"/></svg>
        velmoquartz@mailorb.com
      </li>
      <li class="contacts__item">
        <svg class="contacts__icon" viewBox="0 0 12 12"><circle cx="6" cy="6" r="5.2" fill="none" stroke="var(--blue)" stroke-width="1.1"/><ellipse cx="6" cy="6" rx="2.3" ry="5.2" fill="none" stroke="var(--blue)" stroke-width="1"/><path d="M0.8 6 H11.2" stroke="var(--blue)" stroke-width="1"/></svg>
        www.tunebarrel.com
      </li>
    </ul>

    <div class="socials">
      <ul class="socials__list">
        <li>Viewtrove</li>
        <li>Pagefolk</li>
        <li>Tunebarrel</li>
        <li>Glintory</li>
      </ul>
      <p class="socials__handle">Velmoquartz</p>
    </div>
  </section>
</body>
</html>
```